Marcus Delwyn-Hart Finance

Need a personal website advertising Equipment Finance,Business Finance,Commercial Finance, Construction Finance, Bridging Finance. Similar websites are www.qorvimark.com.au / www.talsbrio.com.au / www.zpk7.com.au /wwwlemberwick.com.au

Target Market(s)

Business People

Industry/Entity Type

Business

Number of Pages Required

3 page

Font styles to use
Serif
Sans Serif

Requirements
Must have
• All i want is a simple corporate looking website advertising Equipment Finance, Commercial Finance, Construction Finance, Business Finance, Bridging Finance,

```html
<!DOCTYPE html>
<html lang="en">
<head>
<meta charset="utf-8">
<title>Marcus Delwyn-Hart Finance</title>
<link href="https://fonts.googleapis.com/css2?family=Open+Sans:wght@400;600;700&display=swap" rel="stylesheet">
<style>
:root{
  --navy:#0f3f63;
  --blue:#1c8fd0;
  --nav:#1a6f9e;
  --dark:#34373c;
  --ink:#333;
  --muted:#666;
  --light:#eef1f4;
  --white:#fff;
  --gold:#f2b01e;
}
*{box-sizing:border-box;margin:0;padding:0}
html,body{width:1200px;height:2316px;overflow:hidden;background:var(--white)}
body{font-family:"Open Sans",Arial,sans-serif;color:var(--ink);position:relative}
.topbar{height:28px;background:var(--navy);color:#cfe2ef;font-size:11px;display:flex;align-items:center;padding:0 132px;justify-content:space-between}
.header{height:84px;display:flex;align-items:center;justify-content:space-between;padding:0 132px}
.brand{display:flex;align-items:center;gap:12px;font-size:30px;color:var(--navy);font-weight:600}
.brand-mark{width:28px;height:28px;background:var(--navy)}
.header-actions{display:flex;gap:24px;align-items:center}
.search{width:300px;height:34px;border:1px solid #b8c7d3;background:#f4f8fb;display:flex;justify-content:flex-end;align-items:center;padding-right:8px}
.btn{display:inline-flex;align-items:center;justify-content:center;background:var(--blue);color:var(--white);font-size:14px;font-weight:600}
.btn-quote{width:124px;height:36px}
.nav{height:48px;background:var(--nav);display:flex;padding:0 132px}
.nav a{color:var(--white);text-decoration:none;font-size:15px;padding:0 26px;line-height:48px}
.nav a.active{background:#3aa5dd}
.hero{height:312px;position:relative;background:linear-gradient(100deg,#c9d6df 0%,#e7edf1 45%,#4b5663 75%,#27303a 100%)}
.hero-caption{position:absolute;left:160px;top:80px;width:288px;height:72px;background:rgba(18,35,50,.88);color:var(--white);font-size:32px;font-weight:700;display:flex;align-items:center;padding-left:22px}
.hero-cta{position:absolute;left:182px;top:166px;width:92px;height:28px;font-size:12px}
.dots{position:absolute;right:240px;bottom:36px;display:flex;gap:8px}
.dots span{width:16px;height:16px;background:var(--nav)}
.dots span:first-child{background:var(--white)}
.intro{text-align:center;font-size:16px;color:var(--muted);line-height:26px;padding-top:38px;width:560px;margin:0 auto;height:120px}
.partners{display:flex;justify-content:center;gap:84px;align-items:center;height:80px;margin-top:0}
.partner{display:flex;align-items:center;gap:10px;font-size:24px;font-weight:600;color:#2d5a86}
.partner i{width:18px;height:18px;border-radius:50%;background:#2d5a86;display:block}
.testimonials{position:absolute;left:0;top:672px;width:1200px;height:392px;background:var(--light)}
.cards{display:flex;gap:20px;position:absolute;left:168px;top:20px}
.card{width:280px;height:290px;background:var(--blue);position:relative}
.avatar{position:absolute;left:24px;top:22px;width:84px;height:84px;border-radius:50%;background:linear-gradient(#d9c2a8,#8c6f58);border:4px solid var(--white)}
.quote-mark{position:absolute;right:26px;top:26px;color:#7cc3ea;font-size:80px;font-weight:700;line-height:1}
.card-body{position:absolute;left:14px;right:14px;top:120px;height:106px;background:var(--white);font-size:12px;color:var(--muted);padding:14px 16px;line-height:18px}
.card-foot{position:absolute;left:14px;right:14px;bottom:14px;height:34px;display:flex;justify-content:space-between;align-items:center;color:var(--white);font-size:13px;font-weight:600}
.stars{color:var(--gold);letter-spacing:2px}
.pager{position:absolute;left:380px;top:342px;display:flex;gap:18px;align-items:center;font-size:13px;color:var(--muted)}
.pager b{width:26px;height:26px;border:1px solid #aaa;display:flex;align-items:center;justify-content:center;font-weight:400}
.pager u{color:var(--ink)}
.options{position:absolute;left:0;top:1092px;width:1200px;height:316px;background:linear-gradient(#3b3e43,#2d3034)}
.section-title{font-size:30px;font-weight:700;color:var(--white);position:absolute;left:132px;top:26px}
.option-list{position:absolute;left:132px;top:98px;display:flex;flex-direction:column;gap:18px}
.option-list span{width:236px;height:40px;display:flex;align-items:center;justify-content:center;font-size:14px;color:var(--white);background:var(--blue)}
.option-list span.current{background:var(--white);color:var(--ink)}
.options p{position:absolute;left:560px;top:94px;width:520px;color:#dcdfe3;font-size:14px;line-height:24px}
.specialist{position:absolute;left:900px;top:254px;width:172px;height:30px;background:var(--white);color:var(--ink);font-size:12px;display:flex;align-items:center;justify-content:center;gap:6px}
.mission{position:absolute;left:0;top:1408px;width:1200px;height:420px}
.mission h2{position:absolute;left:132px;top:64px;font-size:30px;color:var(--navy);font-weight:700}
.mission p{position:absolute;left:132px;top:130px;width:440px;font-size:15px;line-height:24px;color:var(--muted)}
.mission-photo{position:absolute;left:620px;top:112px;width:452px;height:220px;background:linear-gradient(90deg,#5e6a75,#c9b99f 55%,#e8e2d6)}
.keywords{position:absolute;left:0;top:1828px;width:1200px;height:200px;background:linear-gradient(#1e3552,#3a5776 60%,#20314a)}
.keywords .section-title{top:80px}
.kw{position:absolute;left:500px;top:62px;width:560px;display:flex;flex-wrap:wrap;gap:16px 18px}
.kw span{border:1px solid rgba(255,255,255,.6);color:var(--white);font-size:16px;padding:6px 18px}
.footer{position:absolute;left:0;top:2060px;width:1200px;height:184px;padding:0 132px;display:flex;gap:48px;font-size:12px;color:var(--muted)}
.pay h4{font-size:13px;color:var(--ink);margin:20px 0 10px}
.pay-row{display:flex;gap:8px;flex-wrap:wrap;width:160px}
.pay-row span{border:1px solid #ccc;padding:3px 6px;font-size:11px;color:var(--navy);font-weight:600}
.contact{margin-top:22px;display:flex;flex-direction:column;gap:16px;line-height:17px;width:260px}
.contact div{display:flex;gap:10px}
.links{margin-left:auto;margin-top:22px;text-align:right}
.links nav a{color:var(--ink);text-decoration:none;margin-left:18px}
.links nav a:first-child{color:var(--blue)}
.links p{margin-top:8px}
.bottom{position:absolute;left:0;top:2244px;width:1200px;height:72px;border-top:1px solid #ddd;padding:14px 132px;font-size:11px;color:var(--muted);display:flex;justify-content:space-between}
.follow{display:flex;gap:8px;align-items:center}
.follow i{width:20px;height:20px;border-radius:50%;background:#b7c0c8;display:block}
</style>
</head>
<body>
<div class="topbar"><span>E-Book / Downloads Exemption</span><span>T: 1300 555 019</span><span></span></div>
<header class="header">
  <div class="brand"><span class="brand-mark"></span>Marcus Delwyn-Hart Finance</div>
  <div class="header-actions">
    <div class="search"><svg width="16" height="16" viewBox="0 0 16 16"><circle cx="7" cy="7" r="5" fill="none" stroke="#1c8fd0" stroke-width="2"/><line x1="11" y1="11" x2="15" y2="15" stroke="#1c8fd0" stroke-width="2"/></svg></div>
    <span class="btn btn-quote">Quote Now</span>
  </div>
</header>
<nav class="nav"><a class="active">Home</a><a>The Business</a><a>Key People</a><a>Products</a><a>Investors</a><a>Contact Us</a><a>Privacy</a></nav>
<section class="hero" role="img" aria-label="Photo of business people shaking hands in an office">
  <div class="hero-caption">Competitive rates</div>
  <span class="btn hero-cta">Quote Now</span>
  <div class="dots"><span></span><span></span><span></span></div>
</section>
<p class="intro">We compare loan and insurance products from some of Australia's leading finance and insurance companies, including:</p>
<div class="partners">
  <span class="partner">Norvale</span>
  <span class="partner">Pelican Capital</span>
  <span class="partner"><i></i>Westry</span>
  <span class="partner">Daybrook</span>
</div>
<section class="testimonials">
  <div class="cards">
    <article class="card"><div class="avatar" role="img" aria-label="Client portrait"></div><span class="quote-mark">&ldquo;</span><div class="card-body">Fast approval and clear advice. Our new equipment was funded within a week, and the team kept us updated the whole way.</div><div class="card-foot"><span>Lena R Costa</span><span class="stars">★★★★★</span></div></article>
    <article class="card"><div class="avatar" role="img" aria-label="Client portrait"></div><span class="quote-mark">&ldquo;</span><div class="card-body">They found a bridging loan that suited our timing perfectly. Friendly, honest and easy to deal with from start to end.</div><div class="card-foot"><span>Lena R Costa</span><span class="stars">★★★★★</span></div></article>
    <article class="card"><div class="avatar" role="img" aria-label="Client portrait"></div><span class="quote-mark">&ldquo;</span><div class="card-body">Great rates on our commercial loan and no hidden fees. We will certainly use their service again for future projects.</div><div class="card-foot"><span>Lena R Costa</span><span class="stars">★★★★★</span></div></article>
  </div>
  <div class="pager"><b>&lsaquo;</b><span>1/64</span><b>&rsaquo;</b><u>Click Here To View All Testimonials</u></div>
</section>
<section class="options">
  <h2 class="section-title">MY Business Finance Options</h2>
  <div class="option-list"><span class="current">Invoice Factoring</span><span>Trade Finance</span><span>Business Loans</span></div>
  <p>Access 85% of your existing and new invoice value within 24 hours. Waiting to be paid leaves you without cash in the bank and distracts from your focus to take on new opportunities. Pay bills and wages on time with funding that grows with your turnover and not your credit rating. [Learn more] [Step &amp; Apply for a quote]</p>
  <span class="specialist"><svg width="10" height="10" viewBox="0 0 10 10"><path d="M2 1h2l1 2-1 1a5 5 0 0 0 2 2l1-1 2 1v2a1 1 0 0 1-1 1A8 8 0 0 1 1 2a1 1 0 0 1 1-1z" fill="#333"/></svg>Speak with a specialist</span>
</section>
<section class="mission">
  <h2>MY MISSION</h2>
  <p>We aim to provide financial solutions, at turnaround times and levels of efficiency that exceed all other financial institutions. We wish to assist individuals and businesses to achieve long term growth and prosperity. We conduct our business in a professional manner and satisfy our client needs.</p>
  <div class="mission-photo" role="img" aria-label="Photo of a smiling businesswoman in an office"></div>
</section>
<section class="keywords" role="img" aria-label="City skyline at dusk behind the keywords band">
  <h2 class="section-title">MY KEYWORDS</h2>
  <div class="kw"><span>Finance</span><span>Commercial Finance</span><span>Construction Finance</span><span>Business Finance</span><span>Bridging Finance</span></div>
</section>
<footer class="footer">
  <div class="pay"><h4>Payments</h4><div class="pay-row"><span>Payvo</span><span>Visora</span><span>Mintcard</span><span>Amexo</span></div></div>
  <div class="contact">
    <div><svg width="12" height="16" viewBox="0 0 12 16"><path d="M6 0a6 6 0 0 1 6 6c0 4-6 10-6 10S0 10 0 6a6 6 0 0 1 6-6z" fill="#888"/><circle cx="6" cy="6" r="2" fill="#fff"/></svg><span>128 Harlow Drive,<br>Kestrel Bank Queensland 4810</span></div>
    <div><svg width="12" height="16" viewBox="0 0 12 16"><rect x="1" y="0" width="10" height="16" rx="2" fill="#888"/></svg><span>Ph: +61 7 5550 1942<br>Fax: +61 7 5550 1943<br>Email</span></div>
  </div>
  <div class="links"><nav><a>Home</a><a>The Business</a><a>Key People</a><a>Products</a><a>Investors</a><a>Contact Us</a><a>Privacy</a></nav><p>© Book | Downloads Exemption | Privacy Policy | Sitemap</p></div>
</footer>
<div class="bottom"><span>Secured by SSL<br>© 2015 Marcus Delwyn-Hart Finance</span><span class="follow">Follow Us <i></i><i></i><i></i><i></i></span></div>
</body>
</html>
```